Wordpress Design Project

We need a new Wordpress theme for our business Velvora. Velvora specializes in creating custom adult sex toys using CAD and 3D Printing technologies as part of the process. The business's tagline is "Your Pleasure, Your Way".

We are currently using the "Pivot Canvas" theme as a landing page (http://www.velvora.example). We are however we have out grown the single page design and are looking for something new that will allow us to take the next step.

We are looking for something sensual, romantic and sexy, but not something explicit and vulgar.

As the company will be targeting mid to high-end clientele tastefulness is very important to us - this is difficult when the service we are selling is sex but can be achieved.

We would also like for the design to tie in with our current logo and business card designs (Attached).

Target Market(s)

Adults between the ages of 21 and 50 (Predominantly female but not limited to) who like there sex toys and want a custom job.

Industry/Entity Type

Adult

Requirements
Nice to have
• A WordPress design that we particularly like is http://www.tolvane-capital.example/
Should not have
• - Explicit/vulgar illustrations;
- "Clip-Art" should not be used.

```html
<!DOCTYPE html>
<html lang="en">
<head>
<meta charset="utf-8">
<title>Velvora</title>
<link rel="stylesheet" href="https://fonts.googleapis.com/css2?family=Arimo:wght@400;700&display=swap">
<style>
  :root {
    --red: #c83c2f;
    --red-deep: #a52f24;
    --red-line: #8e2519;
    --red-button: #d04a3d;
    --ink-dark: #3d120d;
    --white: #ffffff;
    --side-red: #c0392b;
    --rule: #555555;
  }
  * { margin: 0; padding: 0; box-sizing: border-box; }
  html, body { width: 1200px; height: 780px; overflow: hidden; background: var(--white); }
  body { position: relative; font-family: "Arimo", Arial, sans-serif; }

  .main {
    position: absolute; left: 0; top: 0; width: 840px; height: 780px;
    background: var(--red);
  }
  .hero-band {
    position: absolute; left: 0; top: 100px; width: 840px; height: 200px;
    background: var(--red-deep);
    border-top: 1px solid var(--red-line);
    border-bottom: 1px solid var(--red-line);
  }
  .brand {
    position: absolute; left: 0; top: 158px; width: 840px; text-align: center;
    font-family: "Arimo", Arial, sans-serif; font-weight: 700;
    font-size: 80px; line-height: 1; color: var(--white);
  }
  .intro {
    position: absolute; left: 205px; top: 320px; width: 550px;
    text-align: center; color: var(--white); font-weight: 700; font-size: 13px; line-height: 18px;
  }
  .product-lineup {
    position: absolute; left: 350px; top: 372px; width: 260px; height: 134px;
    background: linear-gradient(90deg, #b9b9b9 0%, #c7a763 35%, #222 50%, #c7a763 62%, #aaa 75%, #6a2a4a 100%);
    border-radius: 14px; opacity: .85;
  }
  .feature {
    position: absolute; top: 530px; width: 240px; height: 151px; text-align: center;
  }
  .feature + .feature { border-left: 1px solid var(--red-line); }
  .feature-icon { height: 72px; display: flex; align-items: center; justify-content: center; margin-top: 2px; }
  .feature-title {
    margin-top: 12px; color: var(--white); font-weight: 700; font-size: 13px; line-height: 15px;
  }
  .learn-more {
    display: block; margin: 8px auto 0; width: 222px; height: 42px; line-height: 40px;
    background: var(--red-button); border: 1px solid var(--ink-dark);
    color: var(--ink-dark); font-weight: 700; font-size: 18px; text-decoration: none;
    box-shadow: 0 1px 2px rgba(0,0,0,.3);
  }

  .sidebar {
    position: absolute; left: 840px; top: 0; width: 360px; height: 780px;
    background: var(--white); box-shadow: -3px 0 5px rgba(0,0,0,.35);
    color: var(--side-red);
  }
  .nav { position: absolute; left: 9px; top: 102px; list-style: none; }
  .nav li { font-size: 14px; height: 30px; line-height: 16px; }
  .nav li:first-child { height: 35px; }
  .nav a { color: var(--side-red); text-decoration: none; }
  .side-block { position: absolute; left: 10px; width: 220px; border-top: 1px solid var(--rule); }
  .side-title { text-align: center; font-weight: 700; font-size: 17px; margin-top: 8px; }
  .contact-row { display: flex; gap: 9px; padding-left: 12px; font-size: 14px; line-height: 17px; }
  .contact-icon { width: 40px; flex: none; display: flex; justify-content: center; padding-top: 8px; }
  .email { font-size: 12px; }
  .social { display: flex; justify-content: center; margin-top: 8px; }
  .social a {
    width: 60px; height: 40px; border-left: 1px solid var(--rule);
    display: flex; align-items: center; justify-content: center;
    color: var(--red-line); font-size: 11px; font-weight: 700; text-decoration: none;
  }
  .social a:last-child { border-right: 1px solid var(--rule); }
</style>
</head>
<body>
  <main class="main">
    <div class="hero-band"></div>
    <div class="brand">Velvora</div>

    <p class="intro">Velvora is making it possible for you to create truly personalised sex toys in the comfort of your own home.</p>
    <div class="product-lineup" role="img" aria-label="Row of seven custom 3D printed toys in silver, gold, black and plum finishes"></div>

    <section class="feature" style="left:120px">
      <div class="feature-icon">
        <svg width="76" height="64" viewBox="0 0 76 64" fill="#fff">
          <rect x="16" y="0" width="44" height="5" rx="2"/>
          <rect x="10" y="8" width="56" height="6" rx="2"/>
          <path d="M2 18h72l-6 40a6 6 0 0 1-6 6H14a6 6 0 0 1-6-6z"/>
          <rect x="24" y="26" width="28" height="10" rx="2" fill="#c83c2f"/>
          <rect x="28" y="26" width="20" height="5" fill="#fff"/>
        </svg>
      </div>
      <div class="feature-title">CHOOSE YOUR TOY DESIGN</div>
      <a class="learn-more" href="#">LEARN MORE</a>
    </section>
    <section class="feature" style="left:360px">
      <div class="feature-icon">
        <svg width="76" height="72" viewBox="0 0 76 72" fill="#fff">
          <path d="M74 2c-4 0-30 26-42 42l6 6C52 36 76 8 74 2z"/>
          <path d="M28 48c-8 0-12 6-12 12 0 4-3 8-10 10 14 2 28-2 29-14z"/>
        </svg>
      </div>
      <div class="feature-title">CUSTOMISE IT AS YOU WISH</div>
      <a class="learn-more" href="#">LEARN MORE</a>
    </section>
    <section class="feature" style="left:600px">
      <div class="feature-icon">
        <svg width="78" height="68" viewBox="0 0 78 68" fill="#fff">
          <rect x="2" y="2" width="74" height="54" rx="7"/>
          <rect x="9" y="9" width="60" height="40" rx="2" fill="#c83c2f"/>
          <path d="M30 56h18l2 8h8v3H20v-3h8z"/>
        </svg>
      </div>
      <div class="feature-title">ALL LIVE ON THE SCREEN</div>
      <a class="learn-more" href="#">LEARN MORE</a>
    </section>
  </main>

  <aside class="sidebar">
    <ul class="nav">
      <li><a href="#" aria-label="Home">
        <svg width="28" height="24" viewBox="0 0 28 24" fill="#c0392b"><path d="M14 0 0 12h4v12h7v-7h6v7h7V12h4z"/></svg>
      </a></li>
      <li><a href="#">Link 1</a></li>
      <li><a href="#">Link 2</a></li>
      <li><a href="#">Link 3</a></li>
      <li><a href="#">Link 4</a></li>
      <li><a href="#">Link 5</a></li>
      <li><a href="#">Link 6</a></li>
    </ul>

    <section class="side-block" style="top:339px">
      <h2 class="side-title">Contact Us</h2>
      <div class="contact-row" style="margin-top:19px">
        <div class="contact-icon">
          <svg width="36" height="34" viewBox="0 0 36 34" fill="#c0392b">
            <rect x="15" y="0" width="4" height="34"/>
            <path d="M19 4h14l3 3-3 3H19z"/>
            <path d="M15 10H4l-4 4 4 4h11z"/>
          </svg>
        </div>
        <div>Your Company,<br>123, Your Street,<br>00000, Your City,<br>Your&nbsp; Country</div>
      </div>
      <div class="contact-row" style="margin-top:12px">
        <div class="contact-icon" style="padding-top:2px">
          <svg width="34" height="22" viewBox="0 0 34 22" fill="#c0392b">
            <path d="M0 0h34v2L17 12 0 2z"/><path d="M0 5l17 10 17-10v17H0z"/>
          </svg>
        </div>
        <div class="email">contact@yourcompany.com</div>
      </div>
    </section>

    <section class="side-block" style="top:529px">
      <h2 class="side-title">Folow Us</h2>
      <nav class="social">
        <a href="#">Chirpline</a>
        <a href="#">Friendfold</a>
      </nav>
    </section>
  </aside>
</body>
</html>
```